Business Card Design

Lawyer
Business name "Halloren Law"
Areas of expertise:
property
commercial
trusts
immigration
franchising
I want the following quote on the back of the card somewhere.
"Education is when you read the fine print,
experience is what you get if you don't." Clem Varnody
Probably the "areas of expertise" should be on the back also to avoid cluttering the front.
As for colours, I like the shades of blue used on qelvobank.com.
The basic part of the card with the contact info needs to be white and uncluttered.
Target Market(s)
small to medium sized self employed business people
Industry/Entity Type
Business
Contact Information for Business Card
Dwight Halloren
Phone + 64 9 415 3067
Fax: + 64 9 415 3066
PO Box 742
Tarewa
Northvale 0627
NZ
email: dwight@ferncastlaw.example.co.nz

```html
<!DOCTYPE html>
<html lang="en">
<head>
<meta charset="utf-8">
<title>Halloren Law Business Card</title>
<link rel="stylesheet" href="https://fonts.googleapis.com/css2?family=Arimo:wght@400;700&display=swap">
<style>
  :root {
    --stage: #2a2a2a;
    --card-white: #ffffff;
    --brand-blue: #0a88c9;
    --ink-grey: #5f6062;
    --rule-grey: #6d6e70;
    --on-blue: #ffffff;
  }
  * { margin: 0; padding: 0; box-sizing: border-box; }
  html, body {
    width: 1200px; height: 557px; overflow: hidden;
    background: var(--stage);
    font-family: "Arimo", Arial, sans-serif;
  }
  .canvas { position: relative; width: 1200px; height: 557px; }
  .card { position: absolute; top: 158px; width: 414px; height: 239px; }
  .card-front { left: 168px; background: var(--card-white); }
  .card-back { left: 617px; background: var(--brand-blue); color: var(--on-blue); }

  .firm-name {
    position: absolute; font-weight: 400; white-space: nowrap; line-height: 1;
  }
  .card-front .firm-name { left: 27px; top: 164px; font-size: 26px; color: var(--brand-blue); }
  .card-back .firm-name { left: 0; width: 100%; text-align: center; top: 76px; font-size: 23px; color: var(--on-blue); }

  .contact { position: absolute; left: 262px; top: 98px; width: 150px; color: var(--ink-grey); }
  .contact-name { color: var(--brand-blue); font-weight: 700; font-size: 12px; margin-bottom: 8px; }
  .contact-line { display: flex; align-items: flex-start; font-size: 9.5px; line-height: 12px; margin-bottom: 3px; white-space: nowrap; }
  .contact-line.email { font-size: 8.6px; }
  .contact-line svg { flex: none; width: 9px; height: 9px; margin: 1px 5px 0 0; fill: var(--brand-blue); }
  .contact-rule { width: 40px; height: 1px; background: var(--rule-grey); margin: 7px 0 10px; }

  .expertise-label { position: absolute; top: 124px; width: 100%; text-align: center; font-size: 8.5px; }
  .expertise-list { position: absolute; top: 138px; width: 100%; text-align: center; font-size: 10.5px; font-weight: 700; }
  .quote { position: absolute; top: 174px; left: 108px; font-size: 10px; line-height: 13px; }
  .quote-source { position: absolute; top: 204px; right: 110px; font-size: 8.5px; }
</style>
</head>
<body>
<main class="canvas">
  <section class="card card-front" aria-label="Card front">
    <div class="firm-name">Halloren Law</div>
    <div class="contact">
      <div class="contact-name">Dwight Halloren</div>
      <div class="contact-line">
        <svg viewBox="0 0 10 10" aria-hidden="true"><path d="M1 3c0-1 1-2 4-2s4 1 4 2v1H7V3H3v1H1zM2 5h6l1 4H1z"/></svg>
        <span>+ 64 9 415 3067</span>
      </div>
      <div class="contact-line">
        <svg viewBox="0 0 10 10" aria-hidden="true"><path d="M3 1h4v3H3zM1 4h8v4H1zM3 7h4v2H3z"/></svg>
        <span>+ 64 9 415 3066</span>
      </div>
      <div class="contact-rule"></div>
      <div class="contact-line">
        <svg viewBox="0 0 10 10" aria-hidden="true"><path d="M5 0l5 3H0zM1 4h1v4H1zM4 4h1v4H4zM6 4h1v4H6zM8 4h1v4H8zM0 9h10v1H0z"/></svg>
        <span>PO Box 742 Tarewa<br>Northvale 0627 NZ</span>
      </div>
      <div class="contact-rule"></div>
      <div class="contact-line email">
        <svg viewBox="0 0 10 10" aria-hidden="true"><path d="M0 2h10v6H0zM1 3l4 3 4-3" stroke="#fff" stroke-width="0.8"/></svg>
        <span>dwight@ferncastlaw.example.co.nz</span>
      </div>
    </div>
  </section>

  <section class="card card-back" aria-label="Card back">
    <div class="firm-name">Halloren Law</div>
    <p class="expertise-label">Areas Of Expertise:</p>
    <p class="expertise-list">Property, Commercial, Trusts, Immigration, Franchising</p>
    <p class="quote">“Education is when you read the fine print,<br>experience is what you get if you don’t.”</p>
    <p class="quote-source">– Clem Varnody</p>
  </section>
</main>
</body>
</html>
```